the halvorsen group premier division

design a DL A4 tri fold brochure to reflect our creative landscape business
my web site www.thehalvorsengroup.com.au
has all the information needed
i will also be updating the website to be more updated and creative design

```html
<!DOCTYPE html>
<html lang="en">
<head>
<meta charset="utf-8">
<title>The Halvorsen Group – Tri-fold Brochure</title>
<link rel="stylesheet" href="https://fonts.googleapis.com/css2?family=Montserrat:ital,wght@0,300;0,400;0,500;0,700;1,300&display=swap">
<style>
  :root{
    --bg:#eeeeec;
    --paper:#ffffff;
    --orange:#f7a21b;
    --orange-deep:#f08a12;
    --blue:#1f5fb8;
    --sky:#2aa3e0;
    --slate:#3a3e48;
    --green:#1f9a45;
    --lime:#8dc63f;
    --ink:#3a3a3a;
    --photo-house:#6b7f9a;
    --photo-garden:#4f7a3c;
    --photo-pool:#2d6fb3;
  }
  *{box-sizing:border-box;margin:0;padding:0}
  html,body{width:1200px;height:1200px;overflow:hidden;background:var(--bg)}
  body{font-family:"Montserrat",sans-serif;color:var(--ink);position:relative}
  .spread{position:absolute;left:230px;width:740px;height:523px;background:var(--paper);overflow:hidden}
  .spread--outside{top:52px}
  .spread--inside{top:625px}
  .spread svg.art{position:absolute;inset:0;width:740px;height:523px}
  .abs{position:absolute}
  .contact-title{left:20px;top:30px;font-size:22px;font-weight:700;color:var(--orange-deep);letter-spacing:.5px}
  .contact-lines{left:20px;top:64px;font-size:7.5px;line-height:15px;color:var(--ink)}
  .social{top:150px;display:flex;flex-direction:column;align-items:center;gap:5px;font-size:5.5px}
  .social .dot{width:18px;height:18px;border-radius:50%;background:var(--orange)}
  .tagline-box{background:#fff;border:1px solid var(--orange);color:var(--orange-deep);font-style:italic;font-weight:300;text-align:center;line-height:1.25}
  .about-box{left:268px;top:24px;width:204px;height:34px;padding:4px;font-size:8.5px}
  .about-box span{display:block;border:1px solid var(--orange);padding:2px}
  .about-text{left:268px;top:72px;width:206px;font-size:7.6px;line-height:10.5px;color:#e8e8e8;text-align:justify}
  .about-text--mid{top:368px}
  .about-text--quote{top:418px;left:292px;width:182px;font-style:italic;font-weight:300}
  .logo{display:flex;flex-direction:column;align-items:center;justify-content:center;text-align:center;font-size:7px;font-weight:700;color:var(--ink);line-height:1.1}
  .cover-title{left:517px;top:338px;font-size:17px;font-weight:500;line-height:24px;color:var(--ink)}
  .cover-box{left:517px;top:392px;width:154px;padding:3px 4px;font-size:9px}
  .cover-url{left:517px;top:432px;font-size:8.5px;font-weight:500}
  .band-label{font-family:"Montserrat",sans-serif;font-size:12px;fill:#fff;letter-spacing:.6px}
  .maint-label{font-family:"Montserrat",sans-serif;font-size:13px;fill:var(--ink);letter-spacing:.8px}
  .inside-box{left:24px;top:476px;width:104px;padding:2px;font-size:5.5px}
  .inside-logo{left:640px;top:482px;width:90px}
</style>
</head>
<body>

<!-- Outside spread -->
<section class="spread spread--outside" aria-label="Brochure outside">
  <svg class="art" viewBox="0 0 740 523">
    <path d="M0,222 C60,175 170,150 232,185 C262,205 240,300 200,360 L140,523 L0,523 Z" fill="var(--orange)"/>
    <path d="M0,232 C60,190 165,168 222,195 C245,212 228,300 190,360 L128,523 L0,523 Z" fill="var(--photo-garden)" role="img" aria-label="Photo of a garden gateway covered in red roses"/>
    <rect x="247" y="0" width="247" height="523" fill="var(--slate)"/>
    <circle cx="370" cy="248" r="68" fill="var(--photo-garden)" role="img" aria-label="Photo of a courtyard garden with outdoor seating"/>
    <circle cx="370" cy="248" r="68" fill="none" stroke="var(--orange)" stroke-width="11"/>
    <rect x="494" y="0" width="246" height="340" fill="var(--photo-house)" role="img" aria-label="Photo of a grand house with a lit swimming pool at dusk"/>
    <rect x="494" y="250" width="246" height="90" fill="var(--photo-pool)"/>
    <path d="M494,0 L740,0 L740,55 C690,30 640,60 600,95 C570,120 530,125 494,110 Z" fill="var(--blue)"/>
    <path d="M494,0 L740,0 L740,40 C690,15 640,45 600,80 C565,108 530,108 494,95 Z" fill="var(--orange)"/>
    <path d="M494,345 C560,320 640,250 740,230 L740,523 L494,523 Z" fill="var(--blue)"/>
    <path d="M494,355 C570,330 650,265 740,248 L740,523 L494,523 Z" fill="#fff"/>
    <path d="M494,523 L494,505 C580,470 660,480 740,488 L740,523 Z" fill="var(--orange)"/>
    <path d="M494,523 L494,515 C590,490 670,500 740,505 L740,523 Z" fill="var(--orange-deep)"/>
    <circle cx="554" cy="40" r="29" fill="#fff"/>
  </svg>

  <h2 class="abs contact-title">CONTACT US</h2>
  <div class="abs contact-lines">
    Erik Halvorsen The Halvorsen Group<br>
    Premier Division<br>
    Postal: PO BOX 42 Eastbrook VIC 3999<br>
    Tel: 0400 000 000<br>
    Email: info@thehalvorsengroup.com.au
  </div>
  <div class="abs social" style="left:14px"><span class="dot"></span>thehalvorsengroup</div>
  <div class="abs social" style="left:88px"><span class="dot"></span>@thgmelb</div>

  <div class="abs tagline-box about-box"><span>Creative Landscape Design<br>and Construction</span></div>
  <p class="abs about-text">The Halvorsen Group (THG), formerly Erik Halvorsen Landscapes, is a professional landscaping and construction service that takes pride in delivering high-end outdoor landscapes across Melbourne, Victoria.</p>
  <p class="abs about-text about-text--mid">THG can work with an existing design or create a landscape design to suit your needs.</p>
  <p class="abs about-text about-text--quote">The Halvorsen Group is a full-service landscaping and construction team that relish the journey to deliver high-end and bespoke outdoor designs.</p>

  <div class="abs logo" style="left:528px;top:18px;width:52px;height:44px">The Halvorsen Group</div>
  <h1 class="abs cover-title">Landscaping to<br>your Lifestyle</h1>
  <div class="abs tagline-box cover-box">Creative Landscape Design<br>and Construction</div>
  <div class="abs cover-url">www.thehalvorsengroup.com.au</div>
</section>

<!-- Inside spread -->
<section class="spread spread--inside" aria-label="Brochure inside">
  <svg class="art" viewBox="0 0 740 523">
    <defs>
      <path id="bandLine" d="M0,248 Q370,160 740,262"/>
      <path id="maintLine" d="M18,350 Q110,400 190,500"/>
    </defs>
    <rect x="0" y="0" width="247" height="300" fill="var(--green)"/>
    <rect x="247" y="0" width="247" height="300" fill="var(--lime)"/>
    <rect x="494" y="0" width="246" height="300" fill="var(--green)"/>
    <circle cx="123" cy="95" r="52" fill="#8a7a66" role="img" aria-label="3D render of a planned backyard design"/>
    <circle cx="370" cy="95" r="52" fill="#7a6a58" role="img" aria-label="Photo of earthworks on a building site"/>
    <circle cx="617" cy="95" r="52" fill="#9aa07a" role="img" aria-label="Photo of a completed garden with a rendered wall"/>
    <g fill="none" stroke="var(--slate)" stroke-width="7">
      <circle cx="123" cy="95" r="52"/><circle cx="370" cy="95" r="52"/><circle cx="617" cy="95" r="52"/>
    </g>
    <path d="M0,270 Q370,185 740,285 L740,523 L0,523 Z" fill="#fff"/>
    <path d="M0,290 Q370,205 740,305 L740,523 L0,523 Z" fill="var(--photo-garden)" role="img" aria-label="Photos of finished gardens with lawn, paving and decking"/>
    <path d="M420,235 Q520,215 600,232 Q560,300 470,290 Q430,270 420,235 Z" fill="#fff"/>
    <path d="M440,242 Q520,226 585,240 Q550,290 480,282 Q448,266 440,242 Z" fill="var(--sky)"/>
    <path d="M0,320 Q160,250 340,350" fill="none" stroke="#fff" stroke-width="9"/>
    <path d="M300,523 Q300,380 470,320 Q600,275 740,300" fill="none" stroke="#fff" stroke-width="9"/>
    <path d="M0,300 Q170,380 290,523 L0,523 Z" fill="#fff"/>
    <path d="M520,523 Q630,440 740,405 L740,523 Z" fill="#fff"/>
    <path d="M0,232 Q370,144 740,246 L740,278 Q370,176 0,264 Z" fill="var(--slate)"/>
    <text class="band-label" dy="4"><textPath href="#bandLine" startOffset="3%">Consultation and Design</textPath></text>
    <text class="band-label" dy="4"><textPath href="#bandLine" startOffset="37%">Earthwork &amp; Site Preparation</textPath></text>
    <text class="band-label" dy="4"><textPath href="#bandLine" startOffset="70%">Installation &amp; Construction</textPath></text>
    <text class="maint-label"><textPath href="#maintLine" startOffset="0%">Maintenance Programs</textPath></text>
    <circle cx="686" cy="466" r="10" fill="var(--orange)"/>
  </svg>
  <div class="abs tagline-box inside-box">Creative Landscape Design<br>and Construction</div>
  <div class="abs logo inside-logo">The Halvorsen Group</div>
</section>

</body>
</html>
```